Cover for Inspirational Daily Journal

This is the cover for a daily journal that will focus on inspirational content for black women. The cover should have a picture or silhouette of a black woman with a crown. The title is: "Grace in Bloom: A Year of Bright Mornings." The back won't have any words. Also the journal will be published on Pagewick.

```html
<!DOCTYPE html>
<html lang="en">
<head>
<meta charset="utf-8">
<title>Grace in Bloom: A Year of Bright Mornings — Journal Cover</title>
<link rel="stylesheet" href="https://fonts.googleapis.com/css2?family=Oswald:wght@300;700&display=swap">
<style>
  :root {
    --backdrop: #d9d9d9;
    --paper-top: #f7ebe6;
    --paper-mid: #f3d2c0;
    --paper-low: #eb9a74;
    --paper-base: #e07a5f;
    --figure-dark: #463a36;
    --figure-mid: #9c5a3f;
    --figure-warm: #c9592e;
    --figure-red: #c0140a;
    --ink: #111111;
    --veil: rgba(255, 255, 255, 0.85);
  }
  * { margin: 0; padding: 0; box-sizing: border-box; }
  html, body {
    width: 1200px;
    height: 1200px;
    overflow: hidden;
    background: var(--backdrop);
  }
  .stage {
    width: 1200px;
    height: 1200px;
    display: flex;
    align-items: center;
    justify-content: center;
  }
  .cover {
    position: relative;
    width: 784px;
    height: 1160px;
    overflow: hidden;
    background:
      linear-gradient(180deg, var(--paper-top) 0%, var(--paper-top) 30%, var(--paper-mid) 60%, var(--paper-low) 88%, var(--paper-base) 100%);
  }
  .cover-art {
    position: absolute;
    left: 0;
    top: 30px;
    width: 560px;
    height: 1130px;
    border-radius: 48% 52% 0 0 / 22% 22% 0 0;
    background:
      linear-gradient(90deg, rgba(255,255,255,0) 0%, rgba(70,58,54,0.25) 100%),
      linear-gradient(180deg, var(--figure-dark) 0%, var(--figure-mid) 40%, var(--figure-warm) 65%, var(--figure-red) 100%);
    opacity: 0.92;
  }
  .veil-lines {
    position: absolute;
    inset: 0;
    pointer-events: none;
  }
  .title,
  .subtitle {
    position: absolute;
    transform-origin: top left;
    white-space: nowrap;
    color: var(--ink);
    font-family: "Oswald", "Arial Narrow", sans-serif;
    line-height: 1;
  }
  .title {
    left: 725px;
    top: 100px;
    transform: rotate(87deg);
    font-weight: 700;
    font-size: 104px;
    text-transform: uppercase;
    letter-spacing: -1px;
  }
  .subtitle {
    left: 622px;
    top: 425px;
    transform: rotate(86deg);
    font-weight: 300;
    font-size: 52px;
    letter-spacing: -0.5px;
  }
</style>
</head>
<body>
  <main class="stage">
    <section class="cover" aria-label="Journal cover">
      <div class="cover-art" role="img" aria-label="Watercolour silhouette of a Black woman in profile wearing a jewelled crown and drop earring, shading from deep brown at the crown to red at the shoulders"></div>
      <svg class="veil-lines" viewBox="0 0 784 1160" aria-hidden="true">
        <path d="M400 0 C 470 300, 520 700, 440 1160" fill="none" stroke="var(--veil)" stroke-width="3"/>
        <path d="M440 0 C 520 320, 560 760, 520 1160" fill="none" stroke="var(--veil)" stroke-width="3"/>
        <path d="M560 0 C 620 360, 640 800, 600 1160" fill="none" stroke="var(--veil)" stroke-width="3"/>
      </svg>
      <h1 class="title">Grace in Bloom:</h1>
      <p class="subtitle">A Year of Bright Mornings.</p>
    </section>
  </main>
</body>
</html>
```